Email Signature

We need a generic email signature designed for our buiding company called 'Birchfield Dwellings'.
We need the following included:
- Name
- Job title (Sales Consultant)
- Phone number
- Mobile number
- Email address
- Physical address
- Web addresss
Please look at the files I have uploaded as these will give you a good idea on our current branding. Our current email signature works well but just needs refreshing! I've also uploaded some images which can be used if needed.
Industry/Entity Type
It Company
Requirements
Nice to have
- If you could incorporate the colours used on the brochure example (contents list) and and arrows on the bottom of the letterhead... just a thought!

```html
<!DOCTYPE html>
<html lang="en">
<head>
<meta charset="utf-8">
<title>Birchfield Dwellings – Email Signature</title>
<link rel="stylesheet" href="https://fonts.googleapis.com/css2?family=Hind:wght@400;500&family=Pinyon+Script&display=swap">
<style>
  :root {
    --paper: #ffffff;
    --ink: #1a1a1a;
    --brand-red: #8e1712;
    --rule-red: #7a1410;
    --icon-bg: #2b2b2b;
  }
  * { margin: 0; padding: 0; box-sizing: border-box; }
  html, body {
    width: 848px;
    height: 1200px;
    overflow: hidden;
    background: var(--paper);
  }
  .canvas {
    position: relative;
    width: 848px;
    height: 1200px;
    background: var(--paper);
    font-family: "Hind", Arial, sans-serif;
    color: var(--ink);
  }
  .signature { position: absolute; left: 0; top: 0; width: 848px; height: 1200px; }

  .sign-off {
    position: absolute;
    left: 50px;
    top: 486px;
    font-family: "Pinyon Script", cursive;
    font-size: 17px;
    color: var(--ink);
  }
  .person-name {
    position: absolute;
    left: 49px;
    top: 511px;
    font-size: 20px;
    font-weight: 400;
    color: var(--brand-red);
    line-height: 1;
  }
  .job-title {
    position: absolute;
    left: 49px;
    top: 536px;
    font-size: 16px;
    line-height: 1;
  }

  .contact-row {
    position: absolute;
    left: 214px;
    top: 533px;
    display: flex;
    align-items: center;
    font-size: 16.5px;
    line-height: 1;
  }
  .contact-item { display: flex; align-items: center; }
  .contact-item + .contact-item { margin-left: 16px; }
  .contact-item svg { width: 20px; height: 18px; margin-right: 6px; flex: none; }
  .contact-item span { padding-top: 3px; }

  .divider {
    position: absolute;
    left: 48px;
    top: 563px;
    width: 726px;
    height: 2px;
    background: var(--rule-red);
  }

  .brand {
    position: absolute;
    left: 104px;
    top: 580px;
    display: flex;
    align-items: center;
  }
  .brand-square {
    width: 52px;
    height: 52px;
    background: var(--brand-red);
    border-radius: 4px;
    margin-right: 14px;
  }
  .brand-name {
    font-size: 44px;
    font-weight: 500;
    color: var(--brand-red);
    line-height: 1;
    padding-top: 8px;
  }

  .postal-address {
    position: absolute;
    left: 55px;
    top: 643px;
    font-size: 13.5px;
    line-height: 1;
  }
  .web-address {
    position: absolute;
    left: 0;
    width: 690px;
    top: 666px;
    text-align: center;
    font-size: 18px;
    line-height: 1;
  }
</style>
</head>
<body>
<div class="canvas">
  <section class="signature" aria-label="Email signature">
    <p class="sign-off">Kind Regards,</p>
    <p class="person-name">Dana Whitmore</p>
    <p class="job-title">Sales Consultant</p>

    <div class="contact-row">
      <div class="contact-item">
        <svg viewBox="0 0 20 18" aria-hidden="true">
          <rect x="0" y="0" width="20" height="18" rx="3" fill="var(--icon-bg)"/>
          <path d="M4 7 q6 -5 12 0 l-1.5 2 -2.5 -1 v-1.5 h-4 v1.5 l-2.5 1 z" fill="#fff"/>
          <rect x="6" y="9.5" width="8" height="5" rx="1" fill="#fff"/>
        </svg>
        <span>03 5550 0142</span>
      </div>
      <div class="contact-item">
        <svg viewBox="0 0 20 18" aria-hidden="true">
          <rect x="0" y="0" width="20" height="18" rx="3" fill="var(--icon-bg)"/>
          <rect x="7" y="3" width="7" height="12" rx="1.5" fill="#fff" transform="rotate(-20 10 9)"/>
          <rect x="8.3" y="5" width="4.4" height="5" fill="var(--icon-bg)" transform="rotate(-20 10 9)"/>
        </svg>
        <span>03 5550 0187</span>
      </div>
      <div class="contact-item">
        <svg viewBox="0 0 20 18" aria-hidden="true">
          <rect x="1" y="3" width="18" height="12" rx="1" fill="#fff" stroke="var(--icon-bg)" stroke-width="1.4"/>
          <path d="M1.5 3.8 L10 10 L18.5 3.8" fill="none" stroke="var(--icon-bg)" stroke-width="1.4"/>
        </svg>
        <span>dana@birchfield.com.au</span>
      </div>
    </div>

    <div class="divider"></div>

    <div class="brand">
      <div class="brand-square"></div>
      <p class="brand-name">Birchfield Dwellings</p>
    </div>

    <p class="postal-address">18, Kestrel Road(Ridge Hwy), Marlow VIC 3999 | PO Number 482, Marlow Victoria 3999</p>
    <p class="web-address">birchfield.com.au</p>
  </section>
</div>
</body>
</html>
```